Business Card Design

We would like to re-design our business cards. Our Company - Quarvel Turbochargers, rebuilds turbochargers and sells replacement parts. Our website is: http://www.quarvelturbochargers.example
We just had our logo changed. I will attach the file. Looking for fresh new/modern business card. We like the colors red, black, white and silver. Black background looks attractive, but not a requirement. The final design should communicate reasonable/competitive prices, top quality and reliability of our products.
Updates
Project Deadline Extended
Reason: Need to finalize the info on the card. Currently working on changing address and email info. Want to make sure it is the correct one before accepting the final design. Unless, this is something that can be changed at a later time..??
Industry/Entity Type
Business
Contact Information for Business Card
QUARVEL TURBOCHARGERS, LLC
20473 Harrow Bend SE
Massillon, OH 44902
Tel: +1-330-555-0142
Fax: +1-330-555-0187
info@QuarvelTurbochargers.example
Our current business card had the following highlights:
*We rebuild all Turbocharges for Automotive, Diesel and Industrial
*Precision Balancing and in-house turbocharger needs
*All Turbocharger replacement parts are made in USA / U.K.
Look and feel
Each slider illustrates characteristics of the customer's brand and the style your logo design should communicate.

```html
<!DOCTYPE html>
<html lang="en">
<head>
<meta charset="utf-8">
<title>Quarvel Turbochargers – Business Card</title>
<link rel="stylesheet" href="https://fonts.googleapis.com/css2?family=Open+Sans:wght@400;600;700;800&display=swap">
<style>
  :root {
    --backdrop: #4a423d;
    --card-black: #1c1c1d;
    --card-edge: #2a2a2b;
    --brand-red: #e3262b;
    --text-white: #f2f2f2;
    --text-grey: #c9c9c9;
    --divider: #6d6d6d;
  }
  * { margin: 0; padding: 0; box-sizing: border-box; }
  html, body { width: 1200px; height: 766px; overflow: hidden; }
  body {
    background: var(--backdrop);
    font-family: "Open Sans", Arial, sans-serif;
    position: relative;
  }
  .card {
    position: absolute;
    width: 510px;
    height: 292px;
    background: var(--card-black);
    border: 1px solid var(--card-edge);
    border-radius: 4px;
    box-shadow: 0 10px 24px rgba(0,0,0,.35);
    overflow: hidden;
  }
  .card--back { left: 50px; top: 237px; }
  .card--front { left: 640px; top: 237px; }

  .wordmark {
    display: flex;
    align-items: center;
    gap: 12px;
    color: var(--text-white);
    font-weight: 800;
    line-height: 1.05;
  }
  .wordmark__dot {
    width: 18px; height: 18px;
    background: var(--brand-red);
    flex: none;
  }
  .card--back .wordmark {
    position: absolute;
    inset: 0;
    justify-content: center;
    font-size: 38px;
  }
  .card--back .wordmark__dot { width: 30px; height: 30px; }

  .card--front .wordmark {
    position: absolute;
    right: 28px; top: 32px;
    font-size: 27px;
  }

  .contact {
    position: absolute;
    left: 18px; right: 16px; top: 136px;
    display: flex;
    align-items: stretch;
    font-size: 12.5px;
    line-height: 1.5;
  }
  .contact__person {
    flex: 1;
    text-align: right;
    padding-right: 14px;
    color: var(--text-grey);
    white-space: nowrap;
  }
  .contact__name {
    color: var(--brand-red);
    font-weight: 600;
    font-size: 20px;
    line-height: 1.3;
  }
  .contact__divider {
    width: 1px;
    background: var(--divider);
    margin-top: 30px;
  }
  .contact__lines {
    list-style: none;
    padding-left: 12px;
    padding-top: 28px;
    color: var(--text-white);
    white-space: nowrap;
  }
  .contact__lines li { display: flex; align-items: center; gap: 8px; }
  .contact__lines svg { width: 11px; height: 11px; fill: var(--brand-red); flex: none; }
</style>
</head>
<body>

<section class="card card--back" aria-label="Card back">
  <div class="wordmark"><span class="wordmark__dot"></span><span>Quarvel<br>Turbochargers</span></div>
</section>

<section class="card card--front" aria-label="Card front">
  <div class="wordmark"><span class="wordmark__dot"></span><span>Quarvel<br>Turbochargers</span></div>

  <div class="contact">
    <div class="contact__person">
      <p class="contact__name">Dorian Vell</p>
      <p>Managing Member</p>
      <p>20473 Harrow Bend SE,</p>
      <p>Massillon, OH 44902</p>
    </div>
    <div class="contact__divider"></div>
    <ul class="contact__lines">
      <li>
        <svg viewBox="0 0 12 12" aria-hidden="true"><path d="M2.5 0.8l2 2.2-1.1 1.4c.7 1.5 1.8 2.6 3.3 3.3l1.4-1.1 2.2 2-1.2 2C5.3 10.6 1.4 6.7 0.8 2z"/></svg>
        <span>+1-330-555-0142</span>
      </li>
      <li>
        <svg viewBox="0 0 12 12" aria-hidden="true"><path d="M3 0h5v3H3z M1 4h10v6H9v2H3v-2H1z M4 8v3h4V8z"/></svg>
        <span>+1-330-555-0187</span>
      </li>
      <li>
        <svg viewBox="0 0 12 12" aria-hidden="true"><path d="M3 0h6v12H3z M4 1.5v8h4v-8z"/></svg>
        <span>+1-330-555-0168</span>
      </li>
      <li>
        <svg viewBox="0 0 12 12" aria-hidden="true"><path d="M0 2h12v1L6 7 0 3z M0 4.4l6 4 6-4V10H0z"/></svg>
        <span>info@QuarvelTurbochargers.example</span>
      </li>
      <li>
        <svg viewBox="0 0 12 12" aria-hidden="true"><path d="M6 0a6 6 0 1 0 0.01 0zM1.3 5.3h2.2c.1-1.5.4-2.8.9-3.7A4.8 4.8 0 0 0 1.3 5.3zm3.4 0h2.6C7.2 3.4 6.6 1.6 6 1.3 5.4 1.6 4.8 3.4 4.7 5.3zm3.8 0h2.2a4.8 4.8 0 0 0-3.1-3.7c.5.9.8 2.2.9 3.7zM1.3 6.7a4.8 4.8 0 0 0 3.1 3.7c-.5-.9-.8-2.2-.9-3.7zm3.4 0c.1 1.9.7 3.7 1.3 4 .6-.3 1.2-2.1 1.3-4zm3.8 0c-.1 1.5-.4 2.8-.9 3.7a4.8 4.8 0 0 0 3.1-3.7z"/></svg>
        <span>www.quarvelturbochargers.example</span>
      </li>
    </ul>
  </div>
</section>

</body>
</html>
```